fun, modern poster design for office environment

We are a Corporate Health consultants and are looking for posters encouraging staff to be healthy.
Wanted: A5 poster design encouraging office workers to take the stairs rather than lift.
Posters will be displayed around the office and near the stairs
Poster will have health benefits included and should have a fun modern feel.
More poster designs to follow.

Target Market(s)

Men and some aged between 20 and 55.

Industry/Entity Type

Environment

Font styles to use
Sans Serif

Colors
0792cd
00a990
9ccb3b
86cfc6
fbf289
fcca95
ffffff
3277b5

Requirements
Must have
• A5 size
• Wording 'take the stairs' and a health benefit of taking be stairs.
• My company logo and name Brightwell Collective
• Web address www.brightwellcollective.com.au
Nice to have
• Images and words
Should not have
• Stick people or people images.

```html
<!DOCTYPE html>
<html lang="en">
<head>
<meta charset="utf-8">
<title>Take the Stairs – Brightwell Collective</title>
<link rel="stylesheet" href="https://fonts.googleapis.com/css2?family=Montserrat:wght@500;700;800&display=swap">
<style>
  :root {
    --backdrop: #f4f2f3;
    --paper: #ffffff;
    --brand-blue: #2a78b8;
    --brand-green: #9ccb3b;
    --white: #ffffff;
  }
  * { box-sizing: border-box; margin: 0; padding: 0; }
  html, body {
    width: 1200px;
    height: 1200px;
    overflow: hidden;
    background: var(--backdrop);
    font-family: "Montserrat", Arial, sans-serif;
  }
  .poster {
    position: absolute;
    left: 310px;
    top: 198px;
    width: 580px;
    height: 804px;
    background: var(--paper);
    box-shadow: 2px 3px 5px rgba(0, 0, 0, 0.18);
    overflow: hidden;
  }
  .poster__title {
    position: absolute;
    top: 110px;
    left: 0;
    width: 100%;
    text-align: center;
    font-weight: 800;
    font-size: 45px;
    line-height: 56px;
    color: var(--brand-blue);
  }
  .poster__field {
    position: absolute;
    left: 0;
    top: 0;
    width: 580px;
    height: 804px;
  }
  .benefit-line {
    position: absolute;
    font-weight: 700;
    font-size: 17px;
    line-height: 18px;
    color: var(--brand-blue);
    text-align: justify;
    text-align-last: justify;
    white-space: nowrap;
  }
  .benefit-line--right { text-align: right; text-align-last: right; }
  .brand {
    position: absolute;
    left: 34px;
    top: 584px;
    width: 300px;
    text-align: center;
    color: var(--white);
  }
  .brand__mark {
    display: block;
    margin: 0 auto 18px;
    width: 108px;
    height: 108px;
    border: 4px solid var(--white);
    border-radius: 50%;
  }
  .brand__name {
    font-weight: 500;
    font-size: 21px;
    line-height: 26px;
  }
  .brand__web {
    margin-top: 6px;
    font-weight: 500;
    font-size: 13px;
  }
</style>
</head>
<body>
  <main class="poster">
    <h1 class="poster__title">TAKE THE STAIRS</h1>

    <svg class="poster__field" viewBox="0 0 580 804" role="img" aria-label="Staircase arrow illustration climbing across a blue field">
      <polygon fill="var(--brand-blue)" points="0,246 580,642 580,804 0,804"/>
    </svg>

    <div class="benefits">
      <p class="benefit-line" style="left:129px;width:403px;top:256px">• BURNS MORE CALORIES PER MINUTE THAN</p>
      <p class="benefit-line" style="left:164px;width:368px;top:283px">JOGGING • REDUCES CARDIO RISK BY</p>
      <p class="benefit-line" style="left:198px;width:334px;top:309px">MORE THAN 30% • HELPS CONTROL</p>
      <p class="benefit-line" style="left:232px;width:300px;top:335px">WEIGHT AND BUILDS MUSCLE</p>
      <p class="benefit-line" style="left:267px;width:265px;top:362px">TONE • SAVES UP TO 15 MINS</p>
      <p class="benefit-line" style="left:301px;width:231px;top:388px">A DAY AND CUTS</p>
      <p class="benefit-line" style="left:336px;width:196px;top:416px">CARBON • EASY TO</p>
      <p class="benefit-line" style="left:370px;width:162px;top:442px">BUILD INTO YOUR</p>
      <p class="benefit-line" style="left:405px;width:127px;top:469px">DAY AND</p>
      <p class="benefit-line" style="left:440px;width:92px;top:495px">MAKE IT</p>
      <p class="benefit-line benefit-line--right" style="left:460px;width:72px;top:521px">DAILY</p>
      <p class="benefit-line benefit-line--right" style="left:470px;width:62px;top:549px">HABIT</p>
    </div>

    <div class="brand">
      <span class="brand__mark"></span>
      <p class="brand__name">Brightwell Collective</p>
      <p class="brand__web">www.brightwellcollective.com.au</p>
    </div>
  </main>
</body>
</html>
```